Corporate Web Redesign Project - coded

We would like redesign/refresh of our current site that would allow us to increase the depth of content and create a high quality impression for visitors.

Current site - http://corvanisystems.example/

A previous web redesign project has improved our site but it has not really reached the level we require.

Our customers are global, blue chip, organisations and a professional, corporate style of site is required.

Please note we would prefer a coded website to a just a design. We are happy to provide a zip of our current site if required.
Updates

                                   

Target Market(s)

Global oil and gas producers, KT, Pardo, Valmira etc.

Industry/Entity Type

It Professional

Requirements
Must have
• Design should support the level of content we currently have in the existing sitemap - although it should be expandable a site design for a large / complex site would not be appropriate

All current content / pages to be reflected in design

Must be visually appealing

Intuitive and clear navigation that is expandable

Display a high level of professionalism

Use a consistent palette of colours that complements our logo

Clean and organized layout

A way to capture visitor’s information or Call to action (i.e. contact link or form) on every page

Prominent Contact Information
Should not have
• Flash

```html
<!DOCTYPE html>
<html lang="en">
<head>
<meta charset="utf-8">
<title>Corvani Systems</title>
<link rel="stylesheet" href="https://fonts.googleapis.com/css2?family=Open+Sans:wght@300;400;600;700&display=swap">
<style>
:root{
  --teal:#2b5e6e;
  --teal-dark:#24515f;
  --ink:#1f4a57;
  --text:#555d60;
  --olive:#8a9a5a;
  --olive-dark:#7d8d50;
  --panel:#dce9ea;
  --white:#ffffff;
}
*{margin:0;padding:0;box-sizing:border-box}
html,body{width:845px;height:1200px;overflow:hidden;background:var(--white)}
body{position:relative;font-family:"Open Sans",sans-serif;color:var(--text)}
.abs{position:absolute}
.brand{left:88px;top:38px;display:flex;align-items:center;gap:8px;color:var(--ink);font-weight:700;font-size:19px;letter-spacing:.5px}
.brand .mark{width:22px;height:22px;border-radius:50%;background:var(--teal)}
.callus{right:91px;top:18px;font-size:12px;color:#5d6668;white-space:nowrap}
.callus b{font-size:15px;font-weight:400;color:var(--ink);margin-left:4px}
.nav{left:0;top:94px;width:845px;height:44px;background:var(--teal)}
.nav ul{list-style:none;display:flex;position:absolute;left:95px;top:13px}
.nav li{color:#e8f0f2;font-size:12.5px;font-weight:300;margin-right:32px}
.search{left:598px;top:104px;width:154px;height:24px;background:var(--white);border-radius:3px;font-size:7px;color:#666;padding:7px 12px}
.search svg{position:absolute;right:9px;top:5px}
.hero{left:0;top:138px;width:845px;height:310px;background:linear-gradient(90deg,#eef1f1 0%,#e6eaea 45%,#dfe3e2 100%)}
.photo{left:420px;top:138px;width:425px;height:310px;background:linear-gradient(90deg,rgba(230,234,234,0) 0%,#e4e0da 35%,#e9e6e1 70%,#d8dde0 100%)}
.hero-title{left:88px;top:168px;width:320px;font-size:24px;font-weight:400;line-height:31px;color:var(--ink)}
.ticks{left:100px;top:236px;list-style:none}
.ticks li{display:flex;align-items:center;gap:9px;font-size:10px;color:#333;height:22.2px;white-space:nowrap}
.more{left:94px;top:355px;width:116px;height:28px;background:var(--white);box-shadow:0 2px 5px rgba(0,0,0,.15);font-size:11.5px;color:var(--ink);text-align:center;line-height:28px}
.dots{left:94px;top:404px;display:flex;gap:7px}
.dots span{width:12px;height:12px;border-radius:50%;background:var(--teal)}
.band{left:0;top:448px;width:845px;height:82px;background:var(--olive)}
.feature{top:448px;height:82px;background:var(--olive-dark);display:flex;align-items:center;gap:8px;padding-left:18px;color:var(--white);font-size:10px;font-weight:600;white-space:nowrap;box-shadow:inset 0 -6px 10px rgba(0,0,0,.08)}
.section-title{font-size:13px;color:var(--ink);font-weight:400}
.about p{font-size:9.3px;line-height:15.5px;color:#6a7174;width:462px;margin-bottom:15px}
.news h3{font-size:10px;font-weight:400;color:#222;margin-top:12px}
.news p{font-size:8px;line-height:12.5px;color:#6a7174;width:212px}
.news em{display:block;font-size:8px;color:#6a7174}
.news .date{font-size:8px;color:#333}
.contact{font-size:8.5px;line-height:15.6px;color:#222}
.contact .region{font-size:10px;color:#333}
.panel{left:555px;top:530px;width:218px;height:314px;background:var(--panel)}
.panel h2{font-size:13px;font-weight:400;color:var(--ink);margin:21px 0 0 20px;padding-bottom:6px;border-bottom:1px solid #b9cfd2;width:191px}
.field{position:absolute;left:20px;width:178px;height:29px;background:var(--white);font-size:8px;color:#999;padding:8px 9px}
.submit{left:73px;top:271px;width:68px;height:27px;background:var(--white);box-shadow:0 2px 4px rgba(0,0,0,.15);font-size:11px;color:var(--ink);text-align:center;line-height:27px}
.clients{left:0;top:925px;width:845px;height:93px;border-top:3px solid #f1f3f3}
.client{position:absolute;top:32px;width:90px;text-align:center;font-size:11px;font-weight:600;color:#6b6f71}
.footer{left:0;top:1018px;width:845px;height:182px;background:var(--teal)}
.flinks{list-style:none;font-size:10px;line-height:17px;color:#e6eef0;font-weight:300}
.touch{left:360px;top:1068px;font-size:14px;color:var(--white);font-weight:300;display:flex;gap:14px;align-items:center}
.fbrand{left:585px;top:1067px;display:flex;align-items:center;gap:8px;color:#e9eff1;font-weight:700;font-size:19px}
.fbrand .mark{width:22px;height:22px;border-radius:50%;background:#c9d3d6}
.bottom{left:0;top:1150px;width:845px;height:50px;background:var(--teal-dark)}
.copy{left:79px;top:1168px;font-size:10px;color:#e6eef0;font-weight:300}
.badge{left:552px;top:1160px;width:190px;height:32px;background:#3a6b7a;border-radius:3px}
.code{left:774px;top:1176px;font-size:9px;color:#cfdde0}
</style>
</head>
<body>

<div class="abs brand"><span class="mark"></span>Corvani Systems</div>
<div class="abs callus">Call Us : <b>1-800-555-0142</b></div>

<nav class="abs nav">
  <ul><li>Home</li><li>News</li><li>About Us</li><li>Solutions</li><li>Contact Us</li></ul>
</nav>
<div class="abs search">Search
  <svg width="13" height="13" viewBox="0 0 13 13"><circle cx="5.5" cy="5.5" r="4" fill="none" stroke="#777" stroke-width="1.2"/><line x1="8.5" y1="8.5" x2="12" y2="12" stroke="#777" stroke-width="1.5"/></svg>
</div>

<section class="abs hero"></section>
<div class="abs photo" role="img" aria-label="Photo of a smiling businessman in a white shirt and blue tie looking through a small square frame"></div>
<h1 class="abs hero-title">Corvani can work with your organization to facilitate:</h1>
<ul class="abs ticks">
  <li><svg width="11" height="11" viewBox="0 0 11 11"><circle cx="5.5" cy="5.5" r="5.5" fill="var(--teal)"/><path d="M3 5.6l1.8 1.8L8 4.2" fill="none" stroke="#fff" stroke-width="1.4"/></svg>Process Mapping and Gap Analysis</li>
  <li><svg width="11" height="11" viewBox="0 0 11 11"><circle cx="5.5" cy="5.5" r="5.5" fill="var(--teal)"/><path d="M3 5.6l1.8 1.8L8 4.2" fill="none" stroke="#fff" stroke-width="1.4"/></svg>Change Management</li>
  <li><svg width="11" height="11" viewBox="0 0 11 11"><circle cx="5.5" cy="5.5" r="5.5" fill="var(--teal)"/><path d="M3 5.6l1.8 1.8L8 4.2" fill="none" stroke="#fff" stroke-width="1.4"/></svg>Project Management</li>
  <li><svg width="11" height="11" viewBox="0 0 11 11"><circle cx="5.5" cy="5.5" r="5.5" fill="var(--teal)"/><path d="M3 5.6l1.8 1.8L8 4.2" fill="none" stroke="#fff" stroke-width="1.4"/></svg>Training</li>
  <li><svg width="11" height="11" viewBox="0 0 11 11"><circle cx="5.5" cy="5.5" r="5.5" fill="var(--teal)"/><path d="M3 5.6l1.8 1.8L8 4.2" fill="none" stroke="#fff" stroke-width="1.4"/></svg>Business and Technical Consulting and Support</li>
</ul>
<div class="abs more">FOR MORE INFO</div>
<div class="abs dots"><span></span><span></span><span></span></div>

<div class="abs band"></div>
<div class="abs feature" style="left:71px;width:186px">
  <svg width="30" height="30" viewBox="0 0 30 30"><circle cx="13" cy="17" r="10" fill="none" stroke="#fff" stroke-width="1.6"/><path d="M13 10v7h5" fill="none" stroke="#fff" stroke-width="1.6"/><rect x="11" y="4" width="4" height="3" fill="#fff"/></svg>Time &amp; Cost Estimation</div>
<div class="abs feature" style="left:257px;width:179px;background:var(--olive);padding-left:15px">
  <svg width="26" height="30" viewBox="0 0 26 30"><rect x="2" y="4" width="20" height="24" fill="none" stroke="#fff" stroke-width="1.6"/><rect x="5" y="7" width="14" height="5" fill="#fff"/><g fill="#fff"><rect x="5" y="15" width="3" height="3"/><rect x="10.5" y="15" width="3" height="3"/><rect x="16" y="15" width="3" height="3"/><rect x="5" y="21" width="3" height="3"/><rect x="10.5" y="21" width="3" height="3"/><rect x="16" y="21" width="3" height="3"/></g></svg>Materials &amp; Cost Controls</div>
<div class="abs feature" style="left:436px;width:149px">
  <svg width="32" height="26" viewBox="0 0 32 26"><path d="M2 3h12l2 2 2-2h12v20H18l-2 2-2-2H2z" fill="none" stroke="#fff" stroke-width="1.6"/><line x1="16" y1="5" x2="16" y2="23" stroke="#fff" stroke-width="1.4"/></svg>Lessons Learned</div>
<div class="abs feature" style="left:585px;width:189px;background:var(--olive)">
  <svg width="26" height="26" viewBox="0 0 26 26"><circle cx="13" cy="8" r="6" fill="#fff"/><path d="M2 25c0-7 5-10 11-10s11 3 11 10z" fill="#fff"/></svg>Services &amp; Consulting</div>

<section class="abs about" style="left:89px;top:548px">
  <h2 class="section-title" style="margin-bottom:12px">ABOUT US</h2>
  <p>From early phase evaluation through planning, execution and post analysis of wells, we deliver the tools, processes and people required to facilitate major performance improvement and cost savings.</p>
  <p>Our solutions are used in more than 30 countries to support operations ranging from a single well to global deployments with Major Operators.</p>
</section>

<section class="abs news" style="left:89px;top:671px">
  <h2 class="section-title">LATEST NEWS</h2>
  <h3>QMX Selected by Kestrel Energy</h3>
  <p>Kestrel Energy Ltd has selected QMX as the solution to provide probabilistic time and cost estimates for its drilling operations.</p>
  <em>Posted By Corvani Admin,</em>
  <div class="date">2013 Aug ,21st&nbsp; GST 22:10</div>
  <h3 style="margin-top:18px">LTX Implementation at Northmere</h3>
  <p>Northmere selects LTX to support its materials, logistics &amp; cost management processes.</p>
  <em>Posted By Corvani Admin,</em>
  <div class="date">2013 Aug ,21st&nbsp; GST 22:10</div>
</section>

<section class="abs contact" style="left:332px;top:671px">
  <h2 class="section-title" style="margin-bottom:9px">CONTACT INFO</h2>
  <div style="padding-left:2px">
    <div class="region">EUROPE</div>
    12 Harbour Row<br>Dunmore<br>DN4 2QT<br>Phone:+44(0)1632 960481<br>Email: eu@corvanisystems.example
    <div class="region" style="margin-top:14px">NORTH AMERICA</div>
    1800 Westfield Blvd<br>Suite 300<br>Marston, TX 77590<br>Phone:(555) 014 2278<br>Email: us@corvanisystems.example
  </div>
</section>

<aside class="abs panel">
  <h2>Quick Contact Form</h2>
  <div class="field" style="top:58px">First name</div>
  <div class="field" style="top:95px">Last Name</div>
  <div class="field" style="top:132px">E-mail</div>
  <div class="field" style="top:170px">Company</div>
  <div class="field" style="top:207px;height:56px">Message</div>
  <div class="abs submit">SUBMIT</div>
</aside>

<section class="abs clients">
  <div class="client" style="left:102px">Valmira</div>
  <div class="client" style="left:195px">Orenda</div>
  <div class="client" style="left:290px">Halvor</div>
  <div class="client" style="left:385px">Kestrel</div>
  <div class="client" style="left:479px">KT</div>
  <div class="client" style="left:573px">Northmere</div>
  <div class="client" style="left:667px">Brannock</div>
</section>

<footer class="abs footer"></footer>
<ul class="abs flinks" style="left:89px;top:1048px"><li>Home</li><li>News</li><li>About Us</li><li>Solutions</li><li>Contact Us</li></ul>
<ul class="abs flinks" style="left:206px;top:1048px"><li>Privacy Policy</li><li>Terms &amp; Conditions</li><li>Legal Notice</li></ul>
<div class="abs touch">Get In Touch
  <svg width="14" height="16" viewBox="0 0 14 16"><path d="M3 1l3 3-2 2c1 3 3 5 5 6l2-2 3 3-2 2C6 14 1 8 1 3z" fill="none" stroke="#fff" stroke-width="1.3"/></svg>
  <svg width="18" height="12" viewBox="0 0 18 12"><rect x="1" y="1" width="16" height="10" fill="none" stroke="#fff" stroke-width="1.3"/><path d="M1 1l8 6 8-6" fill="none" stroke="#fff" stroke-width="1.3"/></svg>
  <svg width="12" height="16" viewBox="0 0 12 16"><path d="M6 15C2 9 1 7 1 5.5a5 5 0 0110 0C11 7 10 9 6 15z" fill="none" stroke="#fff" stroke-width="1.4"/><circle cx="6" cy="5.5" r="1.8" fill="#fff"/></svg>
</div>
<div class="abs fbrand"><span class="mark"></span>Corvani Systems</div>
<div class="abs bottom"></div>
<div class="abs copy">Copyright ©2013&nbsp; Company Name&nbsp;&nbsp; - All rights reserved</div>
<div class="abs badge" role="img" aria-label="Software partner badge"></div>
<div class="abs code">M1</div>

</body>
</html>
```